依頼詳細
新商品「いちご酢」のラベルデザインをお願いします。
画像のビンにシールを張る予定です。
シールの大きさは特に指定はありませんが、後ろに原材料表記のシールが貼ってあるので、
実際に使えるのは縦160mm,幅60mmになります。
ターゲット層は20~30代の女性なので、かわいらしいデザイン希望です。
記載項目
サイズ:縦160mm 幅60mmの間で。
希望イメージ
シンプル 複雑
単色 カラフル
暗い 明るい
日常 高級
遊び心 厳粛
未来的 伝統的
女性的 男性的
希望する色
赤系
納品ファイル
• 高解像度JPG (.jpg)
• イラストレーター形式 (.ai)
補足説明
■ 選んだ理由

従業員の女性スタッフたちが気にいったので。

■ 提案者全員のお礼・コメント

たくさんのご提案、本当にありがとうございました。
またどうぞよろしくお願いいたします。

```html
<!DOCTYPE html>
<html lang="ja">
<head>
<meta charset="utf-8">
<title>いちご酢 ラベル</title>
<link rel="stylesheet" href="https://fonts.googleapis.com/css2?family=Noto+Sans+JP:wght@500;700&family=Playfair+Display:wght@700&family=Cinzel:wght@700&display=swap">
<style>
  :root {
    --pink-top: #f3a3ad;
    --pink-mid: #f7c4c8;
    --pink-fade: #fbe3e4;
    --white: #ffffff;
    --berry-red: #c9172f;
    --deep-red: #b3243b;
    --ribbon-red: #cf3a4d;
    --ribbon-gold: #f2c55c;
    --fruit-red: #e0313f;
    --ink: #1d1d1d;
    --rule: #9a9a9a;
  }
  html, body {
    margin: 0;
    padding: 0;
    width: 1200px;
    height: 3144px;
    overflow: hidden;
    background: var(--white);
  }
  .label {
    position: absolute;
    left: 12px;
    top: 12px;
    width: 1176px;
    height: 3120px;
    border-radius: 588px;
    border: 4px solid var(--rule);
    box-sizing: border-box;
    overflow: hidden;
    background: linear-gradient(180deg, var(--pink-top) 0%, var(--pink-mid) 35%, var(--pink-fade) 62%, var(--white) 72%, var(--white) 100%);
  }
  .carnival-art {
    position: absolute;
    left: 120px;
    top: 40px;
    width: 936px;
    height: 640px;
    border-radius: 50% 50% 30% 30%;
    background: radial-gradient(ellipse at 50% 60%, rgba(243,200,97,0.55) 0%, rgba(207,58,77,0.35) 45%, rgba(243,163,173,0) 75%);
  }
  .ribbon {
    position: absolute;
    left: 0;
    top: 720px;
    width: 1176px;
    height: 170px;
  }
  .ribbon-title {
    position: absolute;
    left: 0;
    width: 1176px;
    top: 742px;
    text-align: center;
    font-family: "Playfair Display", serif;
    font-weight: 700;
    font-size: 92px;
    color: var(--white);
    letter-spacing: 2px;
  }
  .subtitle {
    position: absolute;
    left: 0;
    width: 1176px;
    top: 888px;
    text-align: center;
    font-family: "Cinzel", serif;
    font-weight: 700;
    font-size: 70px;
    letter-spacing: 18px;
    color: var(--deep-red);
  }
  .subtitle-rule {
    position: absolute;
    left: 0;
    top: 940px;
    width: 1176px;
    height: 40px;
  }
  .product-name {
    position: absolute;
    left: 438px;
    top: 1010px;
    width: 300px;
    height: 1230px;
    margin: 0;
    writing-mode: vertical-rl;
    font-family: "Noto Sans JP", sans-serif;
    font-weight: 500;
    font-size: 290px;
    line-height: 300px;
    letter-spacing: 14px;
    color: var(--berry-red);
    -webkit-text-stroke: 12px var(--white);
    paint-order: stroke fill;
    text-shadow: 6px 8px 0 rgba(179,36,59,0.18);
  }
  .fruit-art {
    position: absolute;
    left: 150px;
    top: 2280px;
    width: 876px;
    height: 520px;
    border-radius: 45%;
    background: radial-gradient(ellipse at 28% 55%, var(--fruit-red) 0%, var(--fruit-red) 28%, rgba(224,49,63,0) 46%),
                radial-gradient(ellipse at 72% 55%, var(--fruit-red) 0%, var(--fruit-red) 28%, rgba(224,49,63,0) 46%);
  }
  .tagline {
    position: absolute;
    left: 0;
    width: 1176px;
    top: 2838px;
    text-align: center;
    font-family: "Noto Sans JP", sans-serif;
    font-weight: 500;
    font-size: 56px;
    color: var(--ink);
    margin: 0;
  }
  .dilution {
    position: absolute;
    left: 452px;
    top: 2938px;
    width: 272px;
    height: 84px;
    box-sizing: border-box;
    border: 4px solid var(--ink);
    border-radius: 42px;
    text-align: center;
    font-family: "Noto Sans JP", sans-serif;
    font-weight: 500;
    font-size: 56px;
    line-height: 74px;
    color: var(--ink);
  }
</style>
</head>
<body>
  <main class="label">
    <div class="carnival-art" role="img" aria-label="Circus tent with flag under bursting stars and string lights"></div>

    <svg class="ribbon" viewBox="0 0 1176 170" aria-hidden="true">
      <polygon points="150,40 280,40 280,150 150,150 195,95" fill="var(--ribbon-gold)"/>
      <polygon points="1026,40 896,40 896,150 1026,150 981,95" fill="var(--ribbon-gold)"/>
      <path d="M230,20 Q588,-10 946,20 L946,140 Q588,110 230,140 Z" fill="var(--ribbon-red)"/>
    </svg>
    <div class="ribbon-title">Strawberry</div>

    <div class="subtitle">VINEGAR</div>
    <svg class="subtitle-rule" viewBox="0 0 1176 40" aria-hidden="true">
      <line x1="300" y1="20" x2="550" y2="20" stroke="var(--deep-red)" stroke-width="4"/>
      <line x1="626" y1="20" x2="876" y2="20" stroke="var(--deep-red)" stroke-width="4"/>
      <polygon points="588,2 594,15 608,16 597,25 601,38 588,30 575,38 579,25 568,16 582,15" fill="var(--deep-red)"/>
    </svg>

    <div class="fruit-art" role="img" aria-label="Two watercolour strawberries"></div>

    <h1 class="product-name">いちご酢</h1>

    <p class="tagline">さっぱりとしていて飲みやすい</p>
    <div class="dilution">4倍希釈</div>
  </main>
</body>
</html>
```